velmorix - customer deliverable template

Word Template Design for Client Deliverables

We are looking for a professional and polished Word template for our client deliverables, including RFP responses, business proposals, technical proposals, and workshop reports. The template must be fully aligned with our corporate style and branding.

To kick things off, we'll start with our ML Pathfinder Session deliverable document as the base for the new template. This is a very simple project with very limited effort.

Project Resources
All necessary documentation and assets can be found in the following Brenvault Files folder:
https://files.brenvault.example/share/7kQ2wPzrT9xLmA4vBn8cYdE5fHjU3sR?ref=link

The folder includes:
Assets: A folder containing our logos, corporate color palettes, and other design inspiration to help you understand our style.
For additional inspiration, please visit our website: www.velmorix.cloud

Feel free to ask any questions you may have.

Best regards,

Velmorix Team

```html
<!DOCTYPE html>
<html lang="en">
<head>
<meta charset="utf-8">
<title>Velmorix – Deliverable Template Pages</title>
<link rel="stylesheet" href="https://fonts.googleapis.com/css2?family=Poppins:wght@400;500;600;700;800&display=swap">
<style>
:root{
  --board:#f2f2f4;
  --teal:#1a9e96;
  --teal-deep:#1d7a78;
  --navy:#111a2a;
  --navy-text:#17223b;
  --ink:#333;
  --purple:#7a1f6f;
  --olive:#a89a2a;
  --mint:#c2e7e4;
  --purple-tint:#f3e3f0;
  --olive-tint:#f6f3dc;
  --teal-tint:#e2f4f2;
  --white:#fff;
}
*{margin:0;padding:0;box-sizing:border-box}
html,body{width:1200px;height:1200px;overflow:hidden}
body{background:var(--board);font-family:'Poppins',sans-serif;color:var(--ink);position:relative}

.board-greeting{position:absolute;top:52px;left:0;width:1200px;text-align:center;color:var(--teal);font-weight:700;font-size:25px;letter-spacing:.2px}
.board-note{position:absolute;top:90px;left:40px;width:1120px;text-align:center;font-size:26.5px;line-height:40px;color:#111}

.page{position:absolute;width:268px;height:378px;overflow:hidden;background:var(--white);box-shadow:0 8px 14px rgba(0,0,0,.18)}
.page--cover-dark{left:274px;top:273px;background:linear-gradient(180deg,#1d7a78 0%,#16505a 45%,#111a2a 100%)}
.page--cover-split{left:660px;top:273px}
.page--overview{left:274px;top:696px}
.page--usecases{left:660px;top:696px}

.wordmark{position:absolute;display:flex;align-items:center;gap:3px;font-weight:600}
.wordmark__square{display:block;background:var(--teal)}

.cover-split__band{position:absolute;left:0;top:0;width:268px;height:312px;background:linear-gradient(180deg,#1d7a78 0%,#16505a 50%,#111a2a 100%)}
.cover__title{position:absolute;left:20px;font-weight:800;font-size:24px;line-height:30px;color:var(--white)}
.cover__title-accent{display:block;font-weight:600;color:var(--teal)}
.cover-split .cover__title-accent{color:var(--white)}
.cover__label{position:absolute;left:20px;font-weight:600;font-size:10px;color:var(--white)}
.cover__value{position:absolute;left:20px;font-weight:500;font-size:7.6px;color:var(--white)}
.cover__rule{position:absolute;left:20px;width:87px;height:1.5px;background:var(--white)}
.cover__art{position:absolute;left:0;top:0}

.page-head{position:absolute;left:16px;top:16px;width:236px;height:22px;border-bottom:1.5px solid var(--teal)}
.page-head .wordmark{right:8px;top:2px;font-size:11px;color:var(--navy-text)}
.page-foot{position:absolute;left:16px;top:352px;width:236px;border-top:1.5px solid var(--teal);padding-top:4px;font-size:4.3px;font-weight:600;color:var(--navy-text)}

.section-title{position:absolute;left:16px;font-weight:600;color:var(--teal);font-size:9.6px}
.section-sub{font-size:9.3px;font-weight:500}
.body-copy{position:absolute;left:16px;width:236px;font-size:4.6px;line-height:9.4px;text-align:justify;color:#444}

.phase-cards{position:absolute;left:19px;top:158px;width:230px;display:flex;justify-content:space-between}
.phase-card{width:71px;height:128px;border:1.5px solid;border-radius:6px;padding:4px 4px;text-align:center;box-shadow:0 1px 3px rgba(0,0,0,.15)}
.phase-card h4{font-size:4.6px;font-weight:600;line-height:7px;margin-bottom:4px}
.phase-card p{font-size:3.3px;line-height:5.6px;color:#444}
.phase-card--inspire{border-color:var(--teal)} .phase-card--inspire h4{color:var(--teal)}
.phase-card--discover{border-color:var(--purple)} .phase-card--discover h4{color:var(--purple)}
.phase-card--prioritize{border-color:var(--olive)} .phase-card--prioritize h4{color:var(--olive)}

.phase-flow{position:absolute;left:17px;top:297px;width:231px;height:47px;background:var(--mint);border-radius:6px}
.phase-flow figcaption{position:absolute;left:0;bottom:3px;width:100%;text-align:center;font-size:3.8px;color:#333}

.question-box{position:absolute;left:18px;top:81px;width:232px;height:59px;background:var(--mint);border-radius:4px;padding:6px 10px}
.question-box li{font-size:4.4px;font-weight:600;color:var(--navy-text);line-height:13px;margin-left:8px}

.usecase-list{position:absolute;left:16px;width:232px;display:flex;flex-direction:column;gap:2px}
.usecase{display:flex;height:23px;border:1px solid}
.usecase__phase{width:43px;display:flex;align-items:center;justify-content:center;text-align:center;color:var(--white);font-weight:600;font-size:3.8px;line-height:5.6px;padding:0 2px}
.usecase__body{flex:1;padding:2px 8px;font-size:3.8px;line-height:5.6px;color:var(--navy-text);font-weight:500}
.usecase__body strong{display:block;font-size:4.2px;font-weight:700}
.usecase--inspire{border-color:var(--teal)} .usecase--inspire .usecase__phase{background:var(--teal)} .usecase--inspire .usecase__body{background:var(--teal-tint)}
.usecase--discover{border-color:var(--purple)} .usecase--discover .usecase__phase{background:var(--purple);font-size:3.3px} .usecase--discover .usecase__body{background:var(--purple-tint)}
.usecase--prioritize{border-color:var(--olive)} .usecase--prioritize .usecase__phase{background:var(--olive);font-size:3px} .usecase--prioritize .usecase__body{background:var(--olive-tint)}
</style>
</head>
<body>

<h1 class="board-greeting">Hi VELMORIX TECHNOLOGIES</h1>
<p class="board-note">I shared this sample so you can get an idea of my approach. If you like it, please message me directly in the Briefnest inbox. I’ve understood your brief very well and I can design this template in a professional and beautiful way for you</p>

<!-- Cover, full dark variant -->
<section class="page page--cover-dark cover">
  <div class="wordmark" style="left:76px;top:22px;font-size:20px;color:var(--navy-text)"><span class="wordmark__square" style="width:12px;height:12px"></span>velmorix</div>
  <h2 class="cover__title" style="top:58px">ML Pathfinder<span class="cover__title-accent">Session</span></h2>
  <p class="cover__label" style="top:147px">Customer Name:</p>
  <p class="cover__value" style="top:163px">Fizzwell An Example</p>
  <div class="cover__rule" style="top:180px"></div>
  <p class="cover__label" style="top:188px">Date:</p>
  <p class="cover__value" style="top:204px">00-00-0000</p>
  <svg class="cover__art" width="268" height="378" viewBox="0 0 268 378">
    <defs>
      <radialGradient id="cloudGlowA" cx="55%" cy="40%" r="65%">
        <stop offset="0" stop-color="#7fe3ff"/><stop offset=".45" stop-color="#1f6fd0"/><stop offset="1" stop-color="#0a1a3d"/>
      </radialGradient>
    </defs>
    <circle cx="198" cy="247" r="100" fill="#fff"/>
    <circle cx="198" cy="247" r="92" fill="url(#cloudGlowA)" role="img" aria-label="Glowing cloud computing illustration with data icons over a circuit board"/>
  </svg>
  <div class="wordmark" style="left:16px;top:338px;font-size:14px;color:var(--white)"><span class="wordmark__square" style="width:8px;height:8px"></span>velmorix</div>
</section>

<!-- Cover, split variant -->
<section class="page page--cover-split cover cover-split">
  <div class="cover-split__band"></div>
  <div class="wordmark" style="left:76px;top:16px;font-size:20px;color:var(--white)"><span class="wordmark__square" style="width:12px;height:12px"></span>velmorix</div>
  <h2 class="cover__title" style="top:54px">ML Pathfinder<span class="cover__title-accent">Session</span></h2>
  <p class="cover__label" style="top:121px">Customer Name:</p>
  <p class="cover__value" style="top:137px">Fizzwell An Example</p>
  <div class="cover__rule" style="top:153px"></div>
  <p class="cover__label" style="top:160px">Date:</p>
  <p class="cover__value" style="top:175px">00-00-0000</p>
  <svg class="cover__art" width="268" height="378" viewBox="0 0 268 378">
    <defs>
      <radialGradient id="cloudGlowB" cx="55%" cy="40%" r="65%">
        <stop offset="0" stop-color="#7fe3ff"/><stop offset=".45" stop-color="#1f6fd0"/><stop offset="1" stop-color="#0a1a3d"/>
      </radialGradient>
    </defs>
    <circle cx="184" cy="236" r="118" fill="#fff"/>
    <circle cx="184" cy="236" r="108" fill="url(#cloudGlowB)" role="img" aria-label="Glowing cloud computing illustration with data icons over a circuit board"/>
  </svg>
  <div class="wordmark" style="left:20px;top:340px;font-size:14px;color:var(--navy-text)"><span class="wordmark__square" style="width:8px;height:8px"></span>velmorix</div>
</section>

<!-- Interior page: workshop overview -->
<section class="page page--overview">
  <header class="page-head"><div class="wordmark"><span class="wordmark__square" style="width:6px;height:6px"></span>velmorix</div></header>
  <h3 class="section-title" style="top:46px">01 Workshop Overview:</h3>
  <h3 class="section-title section-sub" style="top:64px">The Three Phases of ML Pathfinder</h3>
  <p class="body-copy" style="top:80px">Our ML Pathfinder Session is designed to cut through the complexity of artificial intelligence and pinpoint its most impactful applications for your business. We believe a successful AI journey starts with a clear vision and a structured approach. That’s why our workshop is built around three distinct, yet interconnected, phases: Inspire, Discover, and Prioritize. This methodical framework ensures we don’t just identify AI possibilities but truly understand their relevance to your operations and map out a viable path to implementation</p>
  <h3 class="section-title" style="top:140px;font-size:8.4px">Our Approach: The Three Phases of ML Pathfinder</h3>
  <div class="phase-cards">
    <article class="phase-card phase-card--inspire"><h4>Inspire: Igniting<br>Possibilities</h4><p>In this dynamic 60-minute opening phase, we broaden your view of AI through real-world examples and success stories tailored to your industry, so you can picture where AI creates tangible value.</p></article>
    <article class="phase-card phase-card--discover"><h4>Discover: Unearthing Core<br>Opportunities</h4><p>In this 60-minute collaborative session, small groups brainstorm AI use cases unique to your business, from optimizing operations to enhancing customer experiences, then select the three most impactful ones.</p></article>
    <article class="phase-card phase-card--prioritize"><h4>Prioritize: Defining Your<br>Strategic Roadmap</h4><p>In this final 60-minute session each team presents its top three use cases. We rank each idea by impact and feasibility, giving a clear, actionable roadmap for your AI journey.</p></article>
  </div>
  <figure class="phase-flow">
    <svg width="231" height="40" viewBox="0 0 231 40" font-family="Poppins, sans-serif" text-anchor="middle">
      <circle cx="71" cy="20" r="15" fill="var(--teal)" stroke="#17223b" stroke-width=".8"/>
      <circle cx="117" cy="20" r="15" fill="var(--purple)" stroke="#17223b" stroke-width=".8"/>
      <circle cx="163" cy="20" r="15" fill="var(--olive)" stroke="#17223b" stroke-width=".8"/>
      <path d="M87 20h12M133 20h12" stroke="#17223b" stroke-width=".7"/>
      <path d="M99 18.5l2 1.5-2 1.5zM145 18.5l2 1.5-2 1.5z" fill="#17223b"/>
      <g fill="#fff" font-size="4.6" font-weight="600"><text x="71" y="19">Inspire</text><text x="117" y="19">Discover</text><text x="163" y="19">Prioritieze</text></g>
      <g fill="#fff" font-size="3.4"><text x="71" y="25">(60 Minutes)</text><text x="117" y="25">(60 Minutes)</text><text x="163" y="25">(60 Minutes)</text></g>
    </svg>
    <figcaption>Figure 1: The Three Phases Of ML Pathfinder</figcaption>
  </figure>
  <footer class="page-foot">ML Pathfinder Session For Fizzwell</footer>
</section>

<!-- Interior page: use cases -->
<section class="page page--usecases">
  <header class="page-head"><div class="wordmark"><span class="wordmark__square" style="width:6px;height:6px"></span>velmorix</div></header>
  <p class="body-copy" style="top:46px;line-height:8.6px;text-align:left">The velmorix AI Business Leaders guided the teams to adopt a positive and creative mindset, encouraging the generation of a high volume of ideas without being constrained by the current situation. We also guided the teams by posing the following key questions</p>
  <ul class="question-box">
    <li>What business outcomes do you want to improve?</li>
    <li>Are your legacy systems and processes holding you back?</li>
    <li>Are you leveraging your data to better manage your business?</li>
    <li>Have you felt the need to use AI in your business?</li>
  </ul>
  <p class="body-copy" style="top:150px">Each team successfully outlined a set of three promising use caces, as follows:</p>
  <h3 class="section-title" style="top:159px;font-size:6px;color:var(--olive)">Discovery Workshop Phase III: Prioritize</h3>
  <div class="usecase-list" style="top:175px">
    <div class="usecase usecase--inspire"><div class="usecase__phase">Inspire: Igniting Possibilities</div><div class="usecase__body"><strong>Employee assistant</strong>A chatbot capable of answering HR questions such as vacation policy or expense reporting policy</div></div>
    <div class="usecase usecase--discover"><div class="usecase__phase">Discover: Unearthing Core Opportunities</div><div class="usecase__body"><strong>Customer Support assistant</strong>A chatbot capable of answering product FAQ such as how to set up the product or when my order will be delivered</div></div>
    <div class="usecase usecase--prioritize"><div class="usecase__phase">Prioritize: Defining Your Strategic Roadmap</div><div class="usecase__body"><strong>Medical appointment reminder</strong>A voice agent that makes automated calls to patients 48 hours in advance to confirm, reschedule, or cancel their appointments</div></div>
  </div>
  <div class="usecase-list" style="top:264px">
    <div class="usecase usecase--inspire"><div class="usecase__phase">Inspire: Igniting Possibilities</div><div class="usecase__body"><strong>Employee assistant</strong>A chatbot capable of answering HR questions such as vacation policy or expense reporting policy</div></div>
    <div class="usecase usecase--discover"><div class="usecase__phase">Discover: Unearthing Core Opportunities</div><div class="usecase__body"><strong>Customer Support assistant</strong>A chatbot capable of answering product FAQ such as how to set up the product or when my order will be delivered</div></div>
    <div class="usecase usecase--prioritize"><div class="usecase__phase">Prioritize: Defining Your Strategic Roadmap</div><div class="usecase__body"><strong>Medical appointment reminder</strong>A voice agent that makes automated calls to patients 48 hours in advance to confirm, reschedule, or cancel their appointments</div></div>
  </div>
  <footer class="page-foot">ML Pathfinder Session For Fizzwell</footer>
</section>

</body>
</html>
```